Personal Trainer and Corporate Health Business

I need a business card for a new company I'm starting in Australia called "Brisk Vitality Partners" I will be providing a Personal training service as well as corporate health in companies.
The service provided is to help promote an active and healthy lifstyle.
The design should communicate a healthy lifestyle and also the benefits that this can have on a personal level and in the corporate environment and the benefits that flow from that.

Target Market(s)

Members of the public and Corporate

Industry/Entity Type

Environment

Requirements
Must have
• Company logo attached
Look and feel fresh and modern

Tag line: "Inspiring better everyday wellbeing"

Lewis Norgate
Managing Director

m: 0417 596 304
e: lewis@briskvitalitypartners.com.au

www.briskvitalitypartners.com.au
Nice to have
• Can be 1 or 2 sided

```html
<!DOCTYPE html>
<html lang="en">
<head>
<meta charset="utf-8">
<title>Brisk Vitality Partners – Business Card Options</title>
<link rel="stylesheet" href="https://fonts.googleapis.com/css2?family=Arimo&family=Montserrat:wght@500;600;700&family=Source+Serif+4:wght@400;700&display=swap">
<style>
  :root {
    --brand-blue: #0b3d8f;
    --brand-green: #8cc43f;
    --stage-grey: #ececec;
    --card-white: #ffffff;
    --label-ink: #333333;
    --sans: "Montserrat", sans-serif;
    --serif: "Source Serif 4", serif;
  }
  * { margin: 0; padding: 0; box-sizing: border-box; }
  html, body { width: 1132px; height: 1200px; overflow: hidden; }
  body { background: var(--stage-grey); position: relative; font-family: var(--sans); }

  .sheet-label { position: absolute; left: 24px; top: 22px; font: 22px/1 "Arimo", sans-serif; color: var(--label-ink); }
  .option-number { position: absolute; left: 84px; font: 32px/1 "Arimo", sans-serif; color: var(--label-ink); }

  .card { position: absolute; left: 142px; width: 844px; background: var(--card-white); overflow: hidden; }
  .card--wave { top: 74px; height: 485px; border-radius: 32px; box-shadow: 0 10px 22px rgba(0,0,0,.35); }
  .card--band { top: 625px; height: 467px; box-shadow: 0 12px 22px rgba(0,0,0,.35); }
  .card > * { position: absolute; }
  .card svg.art { left: 0; top: 0; }

  .brand-name { font-family: var(--serif); font-weight: 700; color: var(--brand-blue); text-align: center; line-height: 1.1; display: flex; flex-direction: column; align-items: center; justify-content: center; gap: 10px; }
  .brand-dot { width: 18px; height: 18px; border-radius: 50%; background: var(--brand-green); }

  /* Option 1 */
  .card--wave .brand-name { left: 52px; top: 41px; width: 320px; height: 170px; font-size: 34px; }
  .card--wave .tagline { left: 30px; width: 380px; text-align: center; font: 700 21px/1 var(--serif); letter-spacing: 1.5px; white-space: nowrap; }
  .tagline--blue { top: 226px; color: var(--brand-blue); }
  .tagline--green { top: 254px; color: var(--brand-green); }
  .card--wave .person-name { left: 499px; top: 114px; font: 600 24px/1 var(--sans); color: var(--brand-blue); }
  .card--wave .person-title { left: 499px; top: 145px; font: 500 25px/1 var(--sans); color: var(--brand-blue); }
  .card--wave .phone { left: 499px; top: 206px; font: 700 25px/1 var(--sans); color: var(--brand-blue); display: flex; align-items: center; gap: 12px; }
  .contact-line { display: flex; align-items: center; gap: 14px; font: 700 25px/1 var(--sans); color: #fff; left: 147px; }
  .contact-line--email { top: 367px; }
  .contact-line--web { top: 407px; }

  /* Option 2 */
  .card--band .headline { left: 0; width: 844px; top: 54px; text-align: center; font: 700 30px/1 var(--serif); color: var(--brand-blue); white-space: nowrap; }
  .card--band .headline span { color: var(--brand-green); }
  .card--band .person-name { left: 125px; top: 160px; font: 700 23px/1 var(--serif); color: var(--brand-blue); }
  .card--band .person-title { left: 125px; top: 191px; font: 400 18px/1 var(--serif); color: var(--brand-blue); }
  .card--band .brand-name { left: 511px; top: 119px; width: 292px; height: 158px; font-size: 32px; }
  .serif-contact { left: 88px; display: flex; align-items: center; gap: 12px; font: 700 27px/1 var(--serif); color: var(--brand-blue); }
  .serif-contact--phone { top: 260px; }
  .serif-contact--email { top: 309px; }
  .card--band .web-address { left: 28px; top: 421px; font: 700 27px/1 var(--serif); color: #fff; }
</style>
</head>
<body>
  <div class="sheet-label">ONE-SIDED</div>

  <div class="option-number" style="top:110px">1</div>
  <section class="card card--wave">
    <svg class="art" width="844" height="485" viewBox="0 0 844 485" aria-hidden="true">
      <path d="M0,335 C140,362 320,332 520,300 C680,276 780,284 844,298 L844,485 L0,485 Z" fill="var(--brand-blue)"/>
      <path d="M0,277 C80,300 170,330 269,340 C170,338 80,322 0,307 Z" fill="var(--brand-green)"/>
      <path d="M554,302 C680,280 790,284 844,292 L844,352 C790,316 680,298 554,302 Z" fill="var(--brand-green)"/>
    </svg>
    <div class="brand-name"><span class="brand-dot"></span>Brisk Vitality<br>Partners</div>
    <div class="tagline tagline--blue">INSPIRING&nbsp; BETTER</div>
    <div class="tagline tagline--green">EVERYDAY WELLBEING</div>
    <div class="person-name">Lewis Norgate</div>
    <div class="person-title">Managing Director</div>
    <div class="phone">
      <svg width="16" height="26" viewBox="0 0 16 26" aria-hidden="true"><rect x="1.5" y="1.5" width="13" height="23" rx="2.5" fill="none" stroke="var(--brand-blue)" stroke-width="2.5"/><line x1="5" y1="20" x2="11" y2="20" stroke="var(--brand-blue)" stroke-width="2"/></svg>
      0417 596 304
    </div>
    <div class="contact-line contact-line--email">
      <svg width="28" height="20" viewBox="0 0 28 20" aria-hidden="true"><rect x="1" y="1" width="26" height="18" fill="none" stroke="#fff" stroke-width="2"/><path d="M1,1 L14,11 L27,1" fill="none" stroke="#fff" stroke-width="2"/></svg>
      lewis@briskvitalitypartners.com.au
    </div>
    <div class="contact-line contact-line--web">
      <svg width="28" height="28" viewBox="0 0 28 28" aria-hidden="true"><g fill="none" stroke="#fff" stroke-width="1.6"><circle cx="14" cy="14" r="12"/><ellipse cx="14" cy="14" rx="5" ry="12"/><line x1="2" y1="14" x2="26" y2="14"/><line x1="14" y1="2" x2="14" y2="26"/></g></svg>
      www.briskvitalitypartners.com.au
    </div>
  </section>

  <div class="option-number" style="top:657px">2</div>
  <section class="card card--band">
    <svg class="art" width="844" height="467" viewBox="0 0 844 467" aria-hidden="true">
      <polygon points="499,467 586,427 844,427 844,467" fill="var(--brand-green)"/>
      <polygon points="0,400 630,400 540,467 0,467" fill="var(--brand-blue)"/>
    </svg>
    <div class="headline">INSPIRING BETTER <span>EVERYDAY WELLBEING</span></div>
    <div class="person-name">Lewis Norgate</div>
    <div class="person-title">Managing Director</div>
    <div class="brand-name"><span class="brand-dot"></span>Brisk Vitality<br>Partners</div>
    <div class="serif-contact serif-contact--phone">
      <svg width="16" height="26" viewBox="0 0 16 26" aria-hidden="true"><rect x="1.5" y="1.5" width="13" height="23" rx="2.5" fill="none" stroke="var(--brand-blue)" stroke-width="2.5"/><line x1="5" y1="20" x2="11" y2="20" stroke="var(--brand-blue)" stroke-width="2"/></svg>
      0417 596 304
    </div>
    <div class="serif-contact serif-contact--email">
      <svg width="26" height="18" viewBox="0 0 26 18" aria-hidden="true"><rect x="1" y="1" width="24" height="16" fill="none" stroke="var(--brand-blue)" stroke-width="2"/><path d="M1,1 L13,10 L25,1" fill="none" stroke="var(--brand-blue)" stroke-width="2"/></svg>
      lewis@briskvitalitypartners.com.au
    </div>
    <div class="web-address">www.briskvitalitypartners.com.au</div>
  </section>
</body>
</html>
```